Automotive spring company needs banner for website

Banner dimensions: 3840 x 880 pixels
Banner need to be consistent with our branding (logo, stationary, colors, fonts, message).
People images should show happiness and it is preferable those people are in or around a car unless it ties into one of the 3 quotes in the must haves below.
Use color blue #4885ed
and gold color #f7d105
Minimal, strong, clean, & tech

Target Market(s)

35-55 male and female

Industry/Entity Type

Auto Repair

Requirements
Must have
• Clickable element for "Shop" or "Make an Appointment"
• "25 Years of Customer Satisfaction" or
• "Get it Done Right by Specialist" or
• "Peace of Mind National Warranty"
• Use our font, Eurostile and/or complimentary font paring

```html
<!DOCTYPE html>
<html lang="en">
<head>
<meta charset="utf-8">
<title>Coilmark Website Banner</title>
<link href="https://fonts.googleapis.com/css2?family=Orbitron:wght@700;900&display=swap" rel="stylesheet">
<style>
  :root {
    --page-bg: #f1f1f1;
    --brand-blue: #4885ed;
    --brand-gold: #f7d105;
    --logo-gold: #e3c11d;
    --ink-dark: #111111;
    --text-white: #ffffff;
  }
  html, body {
    margin: 0;
    padding: 0;
    width: 1200px;
    height: 1200px;
    overflow: hidden;
    background: var(--page-bg);
  }
  .banner {
    position: absolute;
    left: 20px;
    top: 467px;
    width: 1160px;
    height: 265px;
    box-shadow: 0 1px 4px rgba(0,0,0,0.25);
    overflow: hidden;
  }
  .banner-art {
    position: absolute;
    inset: 0;
    display: block;
  }
  .brand-panel {
    position: absolute;
    left: 760px;
    top: 0;
    width: 376px;
    height: 265px;
    text-align: center;
    font-family: "Orbitron", sans-serif;
  }
  .logo-name {
    position: absolute;
    left: 0;
    right: 0;
    top: 36px;
    margin: 0;
    font-size: 40px;
    font-weight: 900;
    line-height: 1;
    letter-spacing: 1px;
    color: var(--logo-gold);
  }
  .logo-rule {
    position: absolute;
    left: 34px;
    right: 34px;
    top: 89px;
    height: 2px;
    background: var(--ink-dark);
  }
  .tagline-rule {
    position: absolute;
    left: 20px;
    right: 20px;
    height: 1px;
    background: linear-gradient(90deg, rgba(255,255,255,0), rgba(255,255,255,0.6), rgba(255,255,255,0));
  }
  .tagline-rule.top { top: 130px; }
  .tagline-rule.bottom { top: 205px; }
  .tagline {
    position: absolute;
    left: 0;
    right: 0;
    top: 140px;
    margin: 0;
    font-size: 19px;
    font-weight: 700;
    line-height: 27px;
    letter-spacing: 0.5px;
    color: var(--text-white);
    text-shadow: 0 1px 2px rgba(0,0,0,0.35);
  }
  .tagline .highlight { color: var(--brand-gold); }
  .cta-button {
    position: absolute;
    left: 50%;
    top: 220px;
    transform: translateX(-50%);
    padding: 0 18px;
    height: 28px;
    line-height: 28px;
    border-radius: 3px;
    background: var(--brand-gold);
    color: var(--ink-dark);
    font-size: 11px;
    font-weight: 700;
    letter-spacing: 1px;
    text-decoration: none;
    white-space: nowrap;
  }
</style>
</head>
<body>
  <section class="banner">
    <svg class="banner-art" viewBox="0 0 1160 265" width="1160" height="265">
      <defs>
        <linearGradient id="photoTones" x1="0" y1="0" x2="1" y2="1">
          <stop offset="0" stop-color="#6b5a3a"/>
          <stop offset="0.35" stop-color="#b08866"/>
          <stop offset="0.6" stop-color="#3a8fb8"/>
          <stop offset="1" stop-color="#3b2d24"/>
        </linearGradient>
      </defs>
      <rect class="photo-area" x="0" y="0" width="780" height="265" fill="url(#photoTones)" role="img" aria-label="Photo of two happy women leaning out of a blue car giving each other a high five, trees in the background"/>
      <rect class="photo-frame" x="6" y="6" width="1148" height="253" fill="none" stroke="rgba(255,255,255,0.45)" stroke-width="0.8"/>
      <path class="brand-panel-shape" d="M752,0 Q690,132 732,265 L1160,265 L1160,0 Z" fill="#4885ed"/>
      <path class="gold-curve" d="M752,0 Q690,132 732,265" fill="none" stroke="#f7d105" stroke-width="4"/>
    </svg>

    <div class="brand-panel">
      <h1 class="logo-name">COILMARK</h1>
      <div class="logo-rule"></div>
      <div class="tagline-rule top"></div>
      <p class="tagline"><span class="highlight">25 Years</span> of Customer<br>Satisfaction</p>
      <div class="tagline-rule bottom"></div>
      <a class="cta-button" href="#appointment">MAKE AN APPOINTMENT</a>
    </div>
  </section>
</body>
</html>
```